Business Card Design for Tarlo Cosmetics

hair extension supplier and mobile technican
make up and make up artistry
cosmetic eye contacts
eye lashes
general facial and hair products

```html
<!DOCTYPE html>
<html lang="en">
<head>
<meta charset="utf-8">
<title>Tarlo Cosmetics – Business Card</title>
<link rel="stylesheet" href="https://fonts.googleapis.com/css2?family=Josefin+Sans:wght@300;400&family=Open+Sans:wght@400&family=Pinyon+Script&display=swap">
<style>
  :root {
    --backdrop: #2b1a12;
    --card: #000000;
    --ink: #ffffff;
    --ink-soft: #c9c9c9;
    --ink-muted: #8a8a8a;
    --rule: #444444;
  }
  * { margin: 0; padding: 0; box-sizing: border-box; }
  html, body { width: 1200px; height: 900px; overflow: hidden; }
  body { background: var(--backdrop); position: relative; font-family: "Open Sans", sans-serif; }

  .card { position: absolute; background: var(--card); color: var(--ink); }

  /* Front */
  .card-front { left: 71px; top: 36px; width: 720px; height: 397px; }
  .front-logo { position: absolute; left: 0; right: 0; top: 118px; text-align: center; }
  .front-logo .wordmark {
    font-family: "Josefin Sans", sans-serif; font-weight: 300;
    font-size: 104px; line-height: 1; letter-spacing: 34px; padding-left: 34px;
  }
  .front-logo .tagline {
    margin-top: 18px;
    font-family: "Josefin Sans", sans-serif; font-weight: 400;
    font-size: 30px; letter-spacing: 25px; padding-left: 25px;
  }

  /* Back */
  .card-back { left: 19px; top: 476px; width: 725px; height: 404px; }
  .back-logo { position: absolute; left: 28px; top: 36px; width: 270px; }
  .back-logo .wordmark {
    font-family: "Josefin Sans", sans-serif; font-weight: 300;
    font-size: 56px; line-height: 1; letter-spacing: 20px;
  }
  .back-logo .tagline {
    margin-top: 10px;
    font-family: "Josefin Sans", sans-serif; font-weight: 400;
    font-size: 17px; letter-spacing: 11.5px;
  }

  .services { position: absolute; left: 330px; top: 40px; display: flex; gap: 4px; }
  .service {
    position: relative; width: 90px; height: 85px;
    border: 1px solid var(--ink-soft);
  }
  .service .photo { position: absolute; inset: 0; }
  .photo-hair { background: linear-gradient(135deg, #6b2b24, #b56a58 55%, #3a1410); }
  .photo-nails { background: linear-gradient(135deg, #8a8a8a, #cfcfcf 50%, #4a4a4a); }
  .photo-eyes { background: linear-gradient(135deg, #d9b38f, #a87752 55%, #3b2a20); }
  .photo-lashes { background: linear-gradient(135deg, #efe6dc, #c8b6a4 55%, #6f7a5a); }
  .service .label {
    position: absolute; left: 0; right: 0; bottom: 0; height: 18px;
    display: flex; justify-content: space-between; align-items: flex-end;
    padding: 0 4px 2px; font-size: 9.5px; color: var(--ink);
  }
  .service .label .brand {
    font-family: "Josefin Sans", sans-serif; font-weight: 400; letter-spacing: 1px;
    border-top: 2px solid var(--ink); line-height: 1.1;
  }
  .service .label .kind { letter-spacing: 1px; align-self: flex-start; margin-top: -6px; }

  .contact { position: absolute; right: calc(725px - 379px); top: 200px; text-align: right; }
  .contact li {
    list-style: none; height: 28.5px; line-height: 20px;
    font-size: 12.5px; color: var(--ink-soft);
  }
  .divider { position: absolute; left: 389px; top: 198px; width: 1px; height: 113px; background: var(--rule); }
  .icons { position: absolute; left: 404px; top: 200px; }
  .icons svg { display: block; margin-bottom: 8.5px; }
  .person-name {
    position: absolute; left: 434px; top: 230px;
    font-family: "Pinyon Script", cursive; font-size: 33px; color: var(--ink-muted);
  }
</style>
</head>
<body>

  <section class="card card-front">
    <div class="front-logo">
      <div class="wordmark">TARLO</div>
      <div class="tagline">COSMETICS</div>
    </div>
  </section>

  <section class="card card-back">
    <div class="back-logo">
      <div class="wordmark">TARLO</div>
      <div class="tagline">COSMETICS</div>
    </div>

    <div class="services">
      <div class="service">
        <div class="photo photo-hair" role="img" aria-label="Photo of glossy red-brown hair"></div>
        <div class="label"><span class="brand">TARLO</span><span class="kind">HAIR</span></div>
      </div>
      <div class="service">
        <div class="photo photo-nails" role="img" aria-label="Photo of decorated silver nails"></div>
        <div class="label"><span class="brand">TARLO</span><span class="kind">NAILS</span></div>
      </div>
      <div class="service">
        <div class="photo photo-eyes" role="img" aria-label="Photo of eye make-up"></div>
        <div class="label"><span class="brand">TARLO</span><span class="kind">EYES</span></div>
      </div>
      <div class="service">
        <div class="photo photo-lashes" role="img" aria-label="Photo of long eyelashes"></div>
        <div class="label"><span class="brand">TARLO</span><span class="kind">LASHES</span></div>
      </div>
    </div>

    <ul class="contact">
      <li>0400 118 207</li>
      <li>12 Harbour ST, Eastvale, WA, 6010</li>
      <li>mira@tarlocosmetics.com.au</li>
      <li>Socialpage.com/ProfileName</li>
    </ul>

    <div class="divider"></div>

    <div class="icons">
      <svg width="18" height="20" viewBox="0 0 18 20" aria-hidden="true">
        <path d="M2 7 Q9 2 16 7 L14 9 L12 7 L6 7 L4 9 Z" fill="#8a8a8a"/>
        <rect x="4" y="10" width="10" height="6" rx="1" fill="#8a8a8a"/>
      </svg>
      <svg width="18" height="20" viewBox="0 0 18 20" aria-hidden="true">
        <path d="M9 2 A5 5 0 0 1 14 7 C14 11 9 17 9 17 C9 17 4 11 4 7 A5 5 0 0 1 9 2 Z" fill="#8a8a8a"/>
        <circle cx="9" cy="7" r="2" fill="#000"/>
      </svg>
      <svg width="18" height="20" viewBox="0 0 18 20" aria-hidden="true">
        <rect x="2" y="5" width="14" height="10" fill="#8a8a8a"/>
        <path d="M2 5 L9 11 L16 5" fill="none" stroke="#000" stroke-width="1.2"/>
      </svg>
      <svg width="18" height="20" viewBox="0 0 18 20" aria-hidden="true">
        <rect x="3" y="3" width="13" height="13" rx="1" fill="#8a8a8a"/>
      </svg>
    </div>

    <div class="person-name">Mira Calloway</div>
  </section>

</body>
</html>
```